Business Card: RW Office Partners - Your tidy answer finder

Business Name: RW Office Partners
Website: www.rwofficepartners.com.au
Email: marisol@rwofficepartners.com.au
Mobile: 61 487 902 346
Facebook: @rwofficepartners
Instrgram: @rwofficepartners

Brading Colours:
HEX
#986474
#ddccd3
#7a8498
#c9d8e4
#000000
#ffffff

Tag Line: Your organised problem solver

Link to DRAFT website:
https://helpdeskhub.sitebuilderx.com/rw-office-partners

About Page from the website:
My name is Marisol Bramwell, and I would love to assist you to become more productive in your day to day and achieve your business and personal goals.
My mission is to give you time, time to work on the important tasks of your business or to be able to spend more time with your family. I will take on the tasks you don’t have time for, don’t know well or simply don’t like to do.
I have an extensive background in Administration, Tender Coordination, Document Control, WHS and Quality Management working primarily in the Construction, Mining and Corporate World.
I am passionate about being organised, having order and making things in your life (and mine) easier! I love to watch something unfold and grow into something amazing! I am known for being the go-to problem solver, the organiser of all things, producing high standards of work even under pressure. I’m also a confident communicator, and I understand that you’re busy running your business.

Target Market(s)

Small to Medium Business who require assistance in their business by a virtual assistant.

Industry/Entity Type

Virtual Assistant

Contact Information for Business Card

Mobile: 61 487 902 346

Font styles to use
Sans Serif

Colors
ffffff

Requirements
Must have
• Branding Colours as outlined.
Contact Details as outlined.
Logo as provided.
Proper contact details - mobile, facebook, instragm, website.
Simple, Elegant, very clean looking.
Should not have
• Note cute with pictures.
Not too girly as still want to market to construction companies.

```html
<!DOCTYPE html>
<html lang="en">
<head>
<meta charset="UTF-8">
<title>RW Office Partners – Business Card</title>
<link rel="stylesheet" href="https://fonts.googleapis.com/css2?family=Montserrat:wght@400;600&display=swap">
<style>
  :root {
    --mauve: #986474;
    --ink: #231f20;
    --slate: #6f7689;
    --paper: #ffffff;
    --backdrop: #c9c8c6;
    --leaf-dark: #2f5a2a;
    --leaf-light: #7fa36a;
  }
  * { margin: 0; padding: 0; box-sizing: border-box; }
  html, body {
    width: 1200px; height: 740px; overflow: hidden;
    background: var(--backdrop);
    font-family: "Montserrat", sans-serif;
  }
  .card {
    position: absolute; top: 228px;
    width: 497px; height: 283px;
  }
  .card-front {
    left: 97px; background: var(--mauve);
    display: flex; flex-direction: column; align-items: center; justify-content: center;
    gap: 10px;
  }
  .brand-name {
    font-weight: 600; font-size: 31px; color: var(--ink);
    letter-spacing: 0.5px; line-height: 1;
  }
  .tagline {
    font-weight: 600; font-size: 15.5px; color: var(--ink);
    text-transform: uppercase; letter-spacing: 0.3px;
  }
  .card-back {
    left: 606px; background: var(--paper);
    border-bottom: 6px solid var(--mauve);
  }
  .portrait {
    position: absolute; left: 54px; top: 76px;
    width: 132px; height: 132px; border-radius: 50%;
    border: 3px solid var(--mauve);
    background: radial-gradient(circle at 50% 40%, var(--leaf-light), var(--leaf-dark));
  }
  .divider {
    position: absolute; left: 203px; top: 82px;
    width: 1.5px; height: 120px; background: var(--mauve);
  }
  .contact-list {
    position: absolute; left: 216px; top: 93px; list-style: none;
  }
  .contact-list li {
    display: flex; align-items: center; gap: 6px;
    height: 19.8px;
    font-size: 13.4px; color: var(--slate); white-space: nowrap;
  }
  .icon { width: 12px; height: 12px; flex: none; }
  .icon-square { width: 11px; height: 11px; background: var(--mauve); border-radius: 2px; flex: none; margin-right: 1px; }
</style>
</head>
<body>
  <section class="card card-front">
    <div class="brand-name">RW Office Partners</div>
    <div class="tagline">Your tidy answer finder</div>
  </section>

  <section class="card card-back">
    <div class="portrait" role="img" aria-label="Portrait photo of Marisol Bramwell in front of green foliage"></div>
    <div class="divider"></div>
    <ul class="contact-list">
      <li>
        <svg class="icon" viewBox="0 0 12 12"><rect x="3" y="0.5" width="6" height="11" rx="1" fill="none" stroke="#986474" stroke-width="1.3"/><circle cx="6" cy="9.5" r="0.7" fill="#986474"/></svg>
        61 487 902 346
      </li>
      <li><span class="icon-square"></span>@rwofficepartners</li>
      <li><span class="icon-square"></span>@rwofficepartners</li>
      <li>
        <svg class="icon" viewBox="0 0 12 12"><rect x="0.5" y="2.5" width="11" height="7" fill="#986474"/><path d="M0.5 2.5 L6 6.5 L11.5 2.5" fill="none" stroke="#fff" stroke-width="1"/></svg>
        marisol@rwofficepartners.com.au
      </li>
      <li>
        <svg class="icon" viewBox="0 0 12 12"><circle cx="6" cy="6" r="5.5" fill="#986474"/><ellipse cx="6" cy="6" rx="2.3" ry="5.5" fill="none" stroke="#fff" stroke-width="0.8"/><line x1="0.5" y1="6" x2="11.5" y2="6" stroke="#fff" stroke-width="0.8"/></svg>
        www.rwofficepartners.com.au
      </li>
    </ul>
  </section>
</body>
</html>
```